PowerPoint Template Design for business consulting company in Silicon Valley

I need a PowerPoint template to use as the starting point for new presentations. I have a logo but now need design that supports this. I've attached a very descriptive PDF that explains exactly what I need. Here is a list of deliverables: 1. PowerPoint Template that I will use as the starter presentation for all new Vantor Bellway presentationsDesigns for the following slides: See picture below for examples of structure:2. Title slide with subtitle3. Section header4. Title and body5. Title and 2 columns6. Title and 3 columns7. One column text8. Editable timeline to show months, or steps for a process9. Bullet design for unordered list (can be graphic)10. Bullet design for ordered list11. Recommended fonts for each design: Title, subtitle, list, captionOPTIONAL: Possible graphic elements to be used for section title slide backgrounds or graphic elements:--Your team / my team / people on project--Goals for project / presentation--Editable Timeline--Speaking--Writing--Listening--People collaborating / helping each otherI am happy to accept proposals for developing these optional elements in a separate project.

Requirements
Must have
• Must be FLAT design.
• Not flashy or garish. Must be subtle.

```html
<!DOCTYPE html>
<html lang="en">
<head>
<meta charset="utf-8">
<title>Vantor Bellway – Presentation Template</title>
<link href="https://fonts.googleapis.com/css2?family=Montserrat:wght@300;400;600;700;800&family=PT+Serif&display=swap" rel="stylesheet">
<style>
:root{
  --bg:#282838;
  --blue:#1d3f97;
  --green:#2f9e44;
  --dgreen:#1b7a3a;
  --teal:#1a8579;
  --grey:#b5b5b5;
  --lightgrey:#c9c9c9;
  --ink:#222;
  --white:#fff;
  --grad:linear-gradient(135deg,#3aa63f 0%,#1a8a78 50%,#1f4fa0 100%);
  --bar:linear-gradient(180deg,#3aa63f 0%,#15877a 50%,#1d3f97 100%);
}
*{margin:0;padding:0;box-sizing:border-box}
html,body{width:1200px;height:1200px;overflow:hidden;background:var(--bg)}
body{position:relative;font-family:"Montserrat",sans-serif;color:var(--ink)}
.slide{position:absolute;background:var(--white);overflow:hidden}
.abs{position:absolute}
.side-bar{position:absolute;top:0;background:var(--bar);border-bottom-left-radius:10px}
.bold{font-weight:800;color:var(--blue);line-height:1}
.light{font-weight:300;color:var(--lightgrey);line-height:1}
.body{font-size:5.4px;line-height:1.55;color:var(--ink)}
.frame{position:absolute;border:1px solid #9cc9a6}
.bands{position:absolute;bottom:0;height:5px;display:flex}
.bands span{display:block;height:100%;border-top-left-radius:5px}
.brand{display:flex;align-items:center;gap:5px;font-weight:600;color:var(--blue);white-space:nowrap}
.brand .dot{border-radius:50%;border:2px solid var(--green)}
.pageno{position:absolute;font-weight:300;color:var(--dgreen);font-size:14px}
</style>
</head>
<body>

<!-- Title slide -->
<section class="slide title-a" style="left:27px;top:158px;width:551px;height:310px;background:linear-gradient(120deg,#cfcfcf,#f1f1f1 45%,#dcdcdc)">
  <div class="abs" role="img" aria-label="Soft grey ink-wash bamboo leaves background" style="inset:0;background:radial-gradient(circle at 10% 80%,#bdbdbd,transparent 45%)"></div>
  <div class="abs" style="left:34px;top:28px;width:497px;height:254px;background:var(--white)"></div>
  <div class="abs" style="left:53px;top:0;width:1px;height:252px;background:var(--green)"></div>
  <div class="abs" style="left:53px;top:252px;width:212px;height:1px;background:var(--green)"></div>
  <h1 class="abs bold" style="left:70px;top:127px;font-size:42px;line-height:1.18">Presetation<br>title here</h1>
  <p class="abs" style="left:294px;top:237px;font-family:'PT Serif',serif;font-size:19px;color:var(--dgreen)">Click to add subtitle</p>
  <div class="abs brand" style="left:418px;top:78px;font-size:15px"><span class="dot" style="width:14px;height:14px"></span>Vantor<br>Bellway</div>
</section>

<!-- Title slide B -->
<section class="slide title-b" style="left:596px;top:158px;width:551px;height:310px">
  <div class="side-bar" style="left:37px;width:24px;height:181px"></div>
  <h1 class="abs bold" style="left:78px;top:84px;font-size:45px">PRESETATION</h1>
  <p class="abs light" style="left:78px;top:134px;font-size:45px">TITLE HERE</p>
  <p class="abs" style="left:77px;top:208px;font-size:14px;color:var(--green)">CLICK TO ADD SUBTITLE</p>
  <div class="abs" style="left:264px;top:216px;width:134px;height:1px;background:var(--green)"></div>
  <div class="abs brand" style="left:482px;top:262px;font-size:9px"><span class="dot" style="width:8px;height:8px;border-width:1.5px"></span>Vantor<br>Bellway</div>
  <div class="bands" style="left:0;width:551px"><span style="width:184px;background:var(--grey);border-radius:0"></span><span style="width:184px;background:var(--dgreen);border-radius:0"></span><span style="width:183px;background:var(--blue);border-radius:0"></span></div>
</section>

<!-- Instructions -->
<section class="slide instructions" style="left:27px;top:484px;width:366px;height:206px">
  <div class="side-bar" style="left:0;width:15px;height:120px"></div>
  <div class="frame" style="left:14px;top:16px;width:338px;height:172px;border-left:none;border-bottom-color:#9cc9a6"></div>
  <h2 class="abs bold" style="left:26px;top:50px;font-size:26px">INSTRUCTIONS</h2>
  <p class="abs light" style="left:26px;top:79px;font-size:26px">FOR USE</p>
  <div class="abs body" style="left:26px;top:111px;width:310px">
    <p>Lorem ipsum dolor sit amet, consectetuer adipiscing elit, sed diam nonummy nibh euismod tincidunt ut laoreet dolore magna aliquam erat volutpat.</p>
    <p style="margin-top:5px"><b>Ut wisi enim ad minim veniam,</b> quis nostrud exerci tation ullamcorper suscipit lobortis nisl ut aliquip ex ea commodo consequat. Duis autem vel eum iriure dolor in hendrerit in vulputate velit esse molestie consequat, vel illum dolore eu feugiat nulla facilisis at vero eros et accumsan et iusto odio dignissim qui blandit praesent luptatum zzril delenit augue duis dolore te feugait nulla facilisi.</p>
    <p>Lorem ipsum dolor sit amet, cons ectetuer adipiscing elit, sed diam nonummy nibh euismod tincidunt ut laoreet dolore magna aliquam erat volutpat. Ut</p>
  </div>
  <div class="bands" style="right:0"><span style="width:50px;background:#ccc"></span><span style="width:50px;background:var(--dgreen);margin-left:-8px"></span><span style="width:46px;background:var(--blue);margin-left:-8px"></span></div>
  <span class="pageno" style="left:347px;top:186px">2</span>
</section>

<!-- Columns -->
<section class="slide columns" style="left:404px;top:484px;width:366px;height:206px">
  <div class="side-bar" style="left:0;width:15px;height:120px"></div>
  <div class="frame" style="left:14px;top:16px;width:338px;height:172px;border-left:none"></div>
  <h2 class="abs" style="left:38px;top:43px;font-size:26px;line-height:1"><span class="bold">TWO</span> <span style="font-weight:300;color:var(--lightgrey)">OR</span> <span class="bold">THREE</span></h2>
  <p class="abs light" style="left:38px;top:69px;font-size:26px">COLUMS</p>
  <div class="abs" style="left:37px;top:102px;width:300px;display:flex;gap:22px">
    <div class="body" style="flex:1"><p style="font-weight:700;color:var(--dgreen);font-size:7.5px;margin-bottom:4px">Heading 1</p>Lorem ipsum dolor sit amet, consectetuer adipiscing elit, sed diam nonummy nibh euismod tincidunt ut laoreet dolore magna aliquam erat volutpat. Ut wisi enim ad minim veniam, quis nostrud</div>
    <div class="body" style="flex:1"><p style="font-weight:700;color:var(--dgreen);font-size:7.5px;margin-bottom:4px">Heading 2</p>Lorem ipsum dolor sit amet, consectetuer adipiscing elit, sed diam nonummy nibh euismod tincidunt ut laoreet dolore magna aliquam erat volutpat. Ut wisi enim ad minim veniam, quis nostrud</div>
    <div class="body" style="flex:1"><p style="font-weight:700;color:var(--dgreen);font-size:7.5px;margin-bottom:4px">Heading 3</p>Lorem ipsum dolor sit amet, consectetuer adipiscing elit, sed diam nonummy nibh euismod tincidunt ut laoreet dolore magna aliquam erat volutpat. Ut wisi enim ad minim veniam, quis nostrud</div>
  </div>
  <div class="bands" style="right:0"><span style="width:50px;background:#ccc"></span><span style="width:50px;background:var(--dgreen);margin-left:-8px"></span><span style="width:46px;background:var(--blue);margin-left:-8px"></span></div>
  <span class="pageno" style="left:347px;top:186px">3</span>
</section>

<!-- Section heading -->
<section class="slide section-head" style="left:780px;top:484px;width:367px;height:206px">
  <div class="abs" style="left:0;top:0;width:232px;height:206px;background:var(--grad)"></div>
  <div class="abs" style="left:28px;top:17px;width:187px;height:1px;background:rgba(255,255,255,.55)"></div>
  <div class="abs" style="left:214px;top:17px;width:1px;height:100px;background:rgba(255,255,255,.55)"></div>
  <div class="abs" style="left:14px;top:135px;width:1px;height:53px;background:rgba(255,255,255,.55)"></div>
  <div class="abs" style="left:14px;top:187px;width:174px;height:1px;background:rgba(255,255,255,.55)"></div>
  <h2 class="abs" style="left:32px;top:77px;font-size:26px;font-weight:800;color:var(--white);line-height:1">HEADING</h2>
  <p class="abs" style="left:32px;top:103px;font-size:26px;font-weight:300;color:var(--white);line-height:1">TITLE</p>
  <svg class="abs" style="left:297px;top:11px" width="58" height="52" viewBox="0 0 58 52" aria-hidden="true">
    <g fill="none" stroke="var(--dgreen)" stroke-width="5"><circle cx="20" cy="26" r="10"/><circle cx="45" cy="13" r="6" stroke-width="3.5"/><circle cx="45" cy="40" r="6" stroke-width="3.5"/></g>
    <g stroke="var(--dgreen)" stroke-width="5" stroke-linecap="round"><path d="M20 9v3M20 40v3M3 26h3M34 26h3M8 14l2 2M30 36l2 2M8 38l2-2M30 16l2-2"/></g>
  </svg>
  <p class="abs body" style="left:254px;top:74px;width:98px;text-align:justify">Lorem ipsum dolor sit amet, consectetuer adipiscing elit, sed diam nonummy nibh euismod tincidunt ut laoreet dolore magna aliquam erat volutpat. Ut wisi enim ad minim veniam, quis nostrud exerci tation ullamcorper suscipit lobortis nisl ut aliquip ex ea commodo consequat. Duis autem vel eum iriure dolor in hendrerit in vulputate velit esse molestie consequat, vel illum dolore eu feugiat nulla facilisis at vero</p>
</section>

<!-- Map slide -->
<section class="slide map" style="left:29px;top:702px;width:366px;height:206px">
  <div class="abs" style="left:50px;top:16px;width:193px;height:1px;background:var(--blue)"></div>
  <div class="abs" style="left:243px;top:16px;width:1px;height:90px;background:var(--blue)"></div>
  <div class="abs" style="left:14px;top:120px;width:1px;height:67px;background:var(--green)"></div>
  <div class="abs" style="left:14px;top:187px;width:172px;height:1px;background:var(--green)"></div>
  <div class="abs" role="img" aria-label="Regional map in green-to-blue gradient with connected icon markers" style="left:8px;top:32px;width:200px;height:150px;border-radius:40% 30% 45% 35%;background:linear-gradient(120deg,#3aa63f,#1a8a78 55%,#1f4fa0)"></div>
  <div class="abs" style="left:232px;top:0;width:134px;height:206px;background:var(--grad)"></div>
  <svg class="abs" style="left:321px;top:10px" width="22" height="36" viewBox="0 0 22 36" aria-hidden="true"><path d="M11 1a10 10 0 0 0-10 10c0 8 10 24 10 24s10-16 10-24A10 10 0 0 0 11 1z" fill="var(--white)"/><circle cx="11" cy="11" r="4.5" fill="none" stroke="var(--teal)" stroke-width="2.5"/></svg>
  <p class="abs" style="left:251px;top:48px;font-size:7.5px;font-weight:700;color:var(--white)">Heading 3</p>
  <p class="abs body" style="left:251px;top:61px;width:96px;color:var(--white);text-align:justify">Lorem ipsum dolor sit amet, consectetuer adipiscing elit, sed diam nonummy nibh euismod tincidunt ut laoreet dolore magna aliquam erat volutpat. Ut wisi enim ad minim veniam, quis nostrud exerci tation ullamcorper suscipit lobortis nisl ut aliquip ex ea commodo consequat. Duis autem vel eum iriure dolor in hendrerit in vulputate velit esse molestie consequat, vel illum dolore</p>
</section>

<!-- List view -->
<section class="slide list" style="left:404px;top:702px;width:366px;height:206px">
  <div class="side-bar" style="left:0;width:15px;height:120px"></div>
  <div class="frame" style="left:14px;top:16px;width:338px;height:172px;border-left:none"></div>
  <h2 class="abs" style="left:27px;top:43px;font-size:32px;line-height:1"><span class="bold">LIST</span> <span style="font-weight:300;color:var(--lightgrey)">VIEW</span></h2>
  <h3 class="abs bold" style="left:26px;top:102px;font-size:19px">UNORDERED</h3>
  <h3 class="abs" style="left:197px;top:102px;font-size:19px;font-weight:800;color:var(--dgreen);line-height:1">ORDERED</h3>
  <ul class="abs" style="left:28px;top:132px;list-style:none;font-size:7px;line-height:10.5px">
    <li><span style="display:inline-block;width:5px;height:5px;border-radius:50%;background:#ccc;margin-right:1px"></span>Lorem ipsum dolor sit amet,</li>
    <li><span style="display:inline-block;width:5px;height:5px;border-radius:50%;background:#ccc;margin-right:1px"></span>Donec gravida massa ut arcu accumsan,</li>
    <li><span style="display:inline-block;width:5px;height:5px;border-radius:50%;background:#ccc;margin-right:1px"></span>Ut elementum ipsum vitae finibus mollis.</li>
    <li><span style="display:inline-block;width:5px;height:5px;border-radius:50%;background:#ccc;margin-right:1px"></span>Quisque vitae magna at gravida ante.</li>
  </ul>
  <ol class="abs" style="left:198px;top:132px;list-style:none;font-size:7px;line-height:10.5px">
    <li><span style="color:var(--green)">1</span>Lorem ipsum dolor sit amet,</li>
    <li><span style="color:var(--green)">2</span>Donec gravida massa ut arcu accumsan,</li>
    <li><span style="color:var(--green)">3</span>Ut elementum ipsum vitae finibus mollis.</li>
    <li><span style="color:var(--green)">4</span>Quisque vitae magna at gravida ante.</li>
  </ol>
  <div class="bands" style="right:0"><span style="width:50px;background:#ccc"></span><span style="width:50px;background:var(--dgreen);margin-left:-8px"></span><span style="width:46px;background:var(--blue);margin-left:-8px"></span></div>
  <span class="pageno" style="left:347px;top:186px">3</span>
</section>

<!-- Timeline -->
<section class="slide timeline" style="left:780px;top:711px;width:367px;height:206px">
  <svg class="abs" style="left:0;top:0" width="260" height="206" viewBox="975 889 325 258" aria-label="Timeline chart 2011 to 2015">
    <rect x="975" y="889" width="325" height="258" fill="var(--blue)"/>
    <path d="M1080 910H1279V1120H993V1050" fill="none" stroke="rgba(255,255,255,.4)" stroke-width="1"/>
    <g>
      <path d="M1020 1098L1043 1042V1098Z" fill="#fff"/><path d="M1043 1042L1070 1098H1043Z" fill="#c9d0e6"/>
      <path d="M1068 1098L1092 1022V1098Z" fill="#fff"/><path d="M1092 1022L1115 1098H1092Z" fill="#c9d0e6"/>
      <path d="M1110 1098L1137 998V1098Z" fill="#fff"/><path d="M1137 998L1160 1098H1137Z" fill="#c9d0e6"/>
      <path d="M1152 1098L1177 1022V1098Z" fill="#fff"/><path d="M1177 1022L1200 1098H1177Z" fill="#c9d0e6"/>
      <path d="M1195 1098L1220 1007V1098Z" fill="#fff"/><path d="M1220 1007L1245 1098H1220Z" fill="#c9d0e6"/>
    </g>
    <rect x="1015" y="1097" width="240" height="3" fill="#fff"/>
    <g fill="var(--green)"><rect x="1022" y="1021" width="32" height="16"/><rect x="1072" y="999" width="32" height="16"/><rect x="1138" y="980" width="32" height="16"/><rect x="1168" y="1006" width="32" height="16"/><rect x="1234" y="1006" width="32" height="16"/></g>
    <g fill="#fff" font-family="Montserrat,sans-serif" font-size="10" text-anchor="middle"><text x="1040" y="1033">40%</text><text x="1090" y="1011">60%</text><text x="1156" y="992">76%</text><text x="1186" y="1018">62%</text><text x="1252" y="1018">73%</text></g>
    <g fill="#fff" font-family="Montserrat,sans-serif" font-size="8.5" font-weight="600" text-anchor="middle"><text x="1048" y="1115">2011</text><text x="1091" y="1115">2012</text><text x="1134" y="1115">2013</text><text x="1176" y="1115">2014</text><text x="1222" y="1115">2015</text></g>
  </svg>
  <h2 class="abs" style="left:26px;top:30px;font-size:26px;color:var(--white);line-height:1"><span style="font-weight:800">TIME</span> <span style="font-weight:300">LINE</span></h2>
  <svg class="abs" style="left:284px;top:86px" width="52" height="36" viewBox="0 0 52 36" aria-hidden="true">
    <g fill="var(--dgreen)"><rect x="6" y="24" width="6" height="11"/><rect x="14" y="20" width="6" height="15"/><rect x="22" y="23" width="6" height="12"/><rect x="30" y="16" width="6" height="19"/><rect x="38" y="13" width="6" height="22"/></g>
    <path d="M2 22L14 12L24 17L46 3" fill="none" stroke="var(--dgreen)" stroke-width="2"/><path d="M40 2H47V9" fill="none" stroke="var(--dgreen)" stroke-width="2"/>
  </svg>
</section>

<!-- Picture slide -->
<section class="slide picture" style="left:404px;top:930px;width:366px;height:206px">
  <div class="side-bar" style="left:0;width:15px;height:120px"></div>
  <h2 class="abs bold" style="left:27px;top:63px;font-size:32px">PICTURE</h2>
  <p class="abs light" style="left:27px;top:94px;font-size:32px">SLIDE</p>
  <p class="abs body" style="left:26px;top:140px;width:170px">Lorem ipsum dolor sit amet, consectetuer adipiscing elit, sed diam nonummy nibh euismod tincidunt ut laoreet dolore magna aliquam erat volutpat.</p>
  <div class="abs" role="img" aria-label="Soft ink-wash landscape with bamboo leaves and pink lotus flowers" style="left:208px;top:0;width:158px;height:206px;background:linear-gradient(90deg,#fff 0%,#eeeef3 35%,#e6dfe8 60%,#d7e6cf 100%)"></div>
</section>

</body>
</html>
```